kn stationary
knbizcards
Simple
Harold T. Pemberly, PhD
CEO
218 Copperfield Lane, Suite 300 Jackson, MS 39211
htp@kestonnetworksllc.com
www.kestonnetworksllc.com

```html
<!DOCTYPE html>
<html lang="en">
<head>
<meta charset="utf-8">
<title>Keston Networks Stationery</title>
<link rel="stylesheet" href="https://fonts.googleapis.com/css2?family=Montserrat:wght@700&family=Open+Sans:wght@400;600&display=swap">
<style>
  :root {
    --backdrop: #e4e2df;
    --paper: #ffffff;
    --ink: #2a2a2a;
    --ink-soft: #666666;
    --accent: #c8102e;
    --accent-pale: #f3d3d8;
    --edge: #d8d6d3;
  }
  * { margin: 0; padding: 0; box-sizing: border-box; }
  html, body { width: 1200px; height: 689px; overflow: hidden; }
  body { background: var(--backdrop); font-family: "Open Sans", Arial, sans-serif; color: var(--ink); position: relative; }
  .sheet { position: absolute; background: var(--paper); box-shadow: 0 2px 6px rgba(0,0,0,.18); }
  .brand { display: flex; align-items: center; gap: 6px; font-family: "Montserrat", Arial, sans-serif; font-weight: 700; color: var(--ink); letter-spacing: .04em; white-space: nowrap; }
  .brand-dot { border-radius: 50%; background: var(--accent); flex: none; }
  .contact { font-size: 6px; line-height: 1.6; color: var(--ink-soft); text-align: center; }
  .contact .label { color: var(--accent); font-weight: 600; }

  .letterhead { left: 65px; top: 41px; width: 440px; height: 600px; }
  .letterhead .brand { position: absolute; left: 40px; top: 36px; font-size: 15px; }
  .letterhead .brand-dot { width: 12px; height: 12px; }
  .letterhead .backdrop-mark { position: absolute; left: 95px; top: 230px; }
  .letterhead .contact { position: absolute; left: 0; right: 0; bottom: 26px; }

  .card { top: 96px; width: 182px; height: 168px; }
  .card-front { left: 533px; }
  .card-back { left: 732px; }
  .card-front .brand { justify-content: center; margin-top: 26px; font-size: 10px; }
  .card-front .brand-dot { width: 8px; height: 8px; }
  .card-front .person { text-align: center; margin-top: 14px; }
  .person-name { font-size: 7px; font-weight: 600; color: var(--accent); }
  .person-title { font-size: 6px; color: var(--ink-soft); }
  .card-front .contact { margin-top: 8px; font-size: 5px; }
  .card-back { display: flex; flex-direction: column; align-items: center; justify-content: center; gap: 40px; }
  .card-back .brand-dot.solo { width: 34px; height: 34px; margin-top: 30px; }
  .card-back .web { font-size: 5px; color: var(--ink-soft); align-self: flex-end; margin-right: 18px; }

  .envelope-back { left: 523px; top: 288px; width: 389px; height: 216px; }
  .envelope-back svg { position: absolute; inset: 0; }
  .envelope-back .brand-dot { position: absolute; left: 182px; top: 36px; width: 26px; height: 26px; }

  .envelope-front { left: 571px; top: 480px; width: 425px; height: 168px; }
  .envelope-front .brand { position: absolute; left: 150px; top: 22px; font-size: 11px; }
  .envelope-front .brand-dot { width: 9px; height: 9px; }
  .envelope-front .corner-mark { position: absolute; right: 50px; bottom: 34px; width: 50px; height: 50px; border-radius: 50%; background: var(--accent-pale); }
  .envelope-front .contact { position: absolute; left: 150px; width: 140px; bottom: 14px; font-size: 5px; }
</style>
</head>
<body>
  <section class="sheet letterhead">
    <div class="brand"><span>KESTON NETWORKS</span><span class="brand-dot"></span></div>
    <svg class="backdrop-mark" width="250" height="250" viewBox="0 0 250 250" aria-hidden="true">
      <defs>
        <radialGradient id="paleFade" cx="50%" cy="50%" r="50%">
          <stop offset="0" stop-color="#f3d3d8"/>
          <stop offset="1" stop-color="#ffffff" stop-opacity="0"/>
        </radialGradient>
      </defs>
      <circle cx="125" cy="125" r="120" fill="url(#paleFade)"/>
    </svg>
    <div class="contact">
      <div>218 Copperfield Lane, Suite 300 Jackson, MS 39211</div>
      <div><span class="label">P:</span> (601) 555-0142 | <span class="label">F:</span> (601) 555-0143</div>
      <div>htp@kestonnetworksllc.com</div>
      <div>www.kestonnetworksllc.com</div>
    </div>
  </section>

  <section class="sheet card card-front">
    <div class="brand"><span>KESTON NETWORKS</span><span class="brand-dot"></span></div>
    <div class="person">
      <div class="person-name">Harold T. Pemberly, PhD</div>
      <div class="person-title">CEO</div>
    </div>
    <div class="contact">
      <div>218 Copperfield Lane, Suite 300 Jackson, MS 39211</div>
      <div><span class="label">P:</span> (601) 555-0142 | <span class="label">F:</span> (601) 555-0143</div>
      <div>htp@kestonnetworksllc.com</div>
      <div>www.kestonnetworksllc.com</div>
    </div>
  </section>

  <section class="sheet card card-back">
    <span class="brand-dot solo"></span>
    <span class="web">www.kestonnetworksllc.com</span>
  </section>

  <section class="sheet envelope-back">
    <svg width="389" height="216" viewBox="0 0 389 216" aria-hidden="true">
      <polyline points="0,0 194,96 389,0" fill="none" stroke="#d8d6d3" stroke-width="1"/>
      <polyline points="0,216 170,120 219,120 389,216" fill="none" stroke="#d8d6d3" stroke-width="1"/>
    </svg>
    <span class="brand-dot"></span>
  </section>

  <section class="sheet envelope-front">
    <div class="brand"><span>KESTON NETWORKS</span><span class="brand-dot"></span></div>
    <span class="corner-mark"></span>
    <div class="contact">
      <div>218 Copperfield Lane, Suite 300 Jackson, MS 39211</div>
      <div><span class="label">P:</span> (601) 555-0142 | <span class="label">F:</span> (601) 555-0143</div>
      <div>htp@kestonnetworksllc.com</div>
      <div>www.kestonnetworksllc.com</div>
    </div>
  </section>
</body>
</html>
```